Computer Training in the Education sector - Letterhead

We need a new letter head to be designed for the company. We provide computer training fro the Education Sector, both primary and private tertiary providers. The colours will need to tie in with the website www.lanternpathlearning.co.nz.
The company name is Lantern Path Co with the tag line of Computer Training for Educators.
The footer will need to have the following detail...
0508 KEY MENTOR
027 813 459
www.lanternpathlearning.co.nz / lessons@lanternpathlearning.co.nz
Updates

Thanks for the designs so far.

Some have watermarks in the background. Please don't worry about using watermarks as I will not be using a watermark in in a final design.
Regards,
Morris

Thank you for all the designs and the effort. There was some great concepts that came through.

Cheers
Morris

Industry/Entity Type

Computer

```html
<!DOCTYPE html>
<html lang="en">
<head>
<meta charset="utf-8">
<title>Lantern Path Co – Letterhead</title>
<link href="https://fonts.googleapis.com/css2?family=Source+Sans+3:wght@400;600&display=swap" rel="stylesheet">
<style>
  :root {
    --paper: #ffffff;
    --ink: #231f20;
    --ink-soft: #3a3a3a;
    --brand-blue: #2f78bf;
    --brand-orange: #e8833a;
    --rule: #4a4a4a;
  }
  html, body {
    margin: 0;
    padding: 0;
    width: 1034px;
    height: 1200px;
    overflow: hidden;
    background: var(--paper);
  }
  .letterhead {
    position: relative;
    width: 1034px;
    height: 1200px;
    background: var(--paper);
    font-family: "Source Sans 3", "Myriad Pro", sans-serif;
    color: var(--ink);
  }
  .brand {
    position: absolute;
    left: 56px;
    top: 82px;
    display: flex;
    align-items: center;
    gap: 12px;
  }
  .brand-dot {
    width: 34px;
    height: 34px;
    border-radius: 50%;
    background: var(--brand-orange);
  }
  .brand-name {
    font-size: 30px;
    font-weight: 600;
    color: var(--brand-blue);
    line-height: 1;
    white-space: nowrap;
  }
  .tagline {
    position: absolute;
    right: 52px;
    top: 86px;
    margin: 0;
    font-size: 27px;
    font-weight: 400;
    color: var(--ink);
    letter-spacing: 0.1px;
  }
  .footer-rule {
    position: absolute;
    left: 197px;
    top: 1116px;
    width: 668px;
    height: 4px;
  }
  .contact {
    position: absolute;
    left: 100px;
    right: 71px;
    top: 1137px;
    display: flex;
    justify-content: space-between;
    align-items: center;
    margin: 0;
    padding: 0;
    list-style: none;
    font-size: 15px;
    color: var(--ink-soft);
  }
  .contact-divider {
    width: 1px;
    height: 19px;
    background: var(--ink-soft);
  }
</style>
</head>
<body>
  <main class="letterhead">
    <header>
      <div class="brand">
        <span class="brand-dot"></span>
        <span class="brand-name">Lantern Path Co</span>
      </div>
      <h1 class="tagline">Computer Training for Educators</h1>
    </header>

    <footer>
      <svg class="footer-rule" viewBox="0 0 668 4" preserveAspectRatio="none" aria-hidden="true">
        <path d="M0 2 Q334 0.4 668 2 Q334 3.6 0 2 Z" fill="var(--rule)"/>
      </svg>
      <ul class="contact">
        <li>P: 0508 KEY MENTOR</li>
        <li class="contact-divider" aria-hidden="true"></li>
        <li>P: 027 813 459</li>
        <li class="contact-divider" aria-hidden="true"></li>
        <li>E: lessons@lanternpathlearning.co.nz</li>
        <li class="contact-divider" aria-hidden="true"></li>
        <li>W: www.lanternpathlearning.co.nz</li>
      </ul>
    </footer>
  </main>
</body>
</html>
```